Dentist logo, business card and website

I have done an amateur job of creating a logo, business card and website. I would like it to look more professional. the current website can be found at www.benotrelu.com - I would like the website to be built and run through plomsite.com. The content on the website is as I would like it but I am open to suggestions.

The logo should be simple, may be best to keep to the letter BT - maybe to look like the V is a reflection of the A? Again, I am open to suggestions (I have attached a couple of images I have used on presentations but I would like the logo that you design to have a 'no fill' background so it can be placed on slides (for presentations etc).

The colour scheme seems wrong for a dentist, perhaps duck egg with black writing would be better? This applies to the business card as well (I have attached a PDF of some I have had made in the past but again they look amateur and colour scheme is wrong. The business cards should be landscape, have the logo in the top right corner, my name and qualifications in the middle, and my website and physical address in the bottom left corner: Pencoed Dental Surgery, 41-43 Ffordd Glas, Cardiff CF23 9QL.

Target Market(s)

30-60 year olds

Industry/Entity Type

Dental

Contact Information for Business Card

Please see brief and uploads.

Logo Text

BT

Number of Pages Required

4 page

Font styles to use
Decorative
Script

Requirements
Must have
• A sophisticated mature feel.
Nice to have
• Simplicity.
Should not have
• Anything too complicated.

```html
<!DOCTYPE html>
<html lang="en">
<head>
<meta charset="utf-8">
<title>Ben Otrelu – About Me</title>
<link href="https://fonts.googleapis.com/css2?family=Lustria&display=swap" rel="stylesheet">
<style>
  :root {
    --ink: #0a0a0a;
    --paper: #ecebe6;
    --gold: #a2865a;
    --white: #ffffff;
    --photo-light: #e4e0dc;
    --photo-dark: #4e6488;
  }
  * { margin: 0; padding: 0; box-sizing: border-box; }
  html, body { width: 1200px; height: 1000px; overflow: hidden; }
  body {
    position: relative;
    background: var(--ink);
    font-family: "Lustria", Georgia, serif;
    color: var(--ink);
  }
  .site-header {
    position: absolute; top: 110px; left: 0;
    width: 1200px; height: 112px;
    background: var(--paper);
  }
  .brand-name {
    position: absolute; top: 71px; left: 0; width: 1200px;
    text-align: center; color: var(--gold); font-size: 17px;
  }
  .main-nav {
    position: absolute; top: 222px; left: 0;
    width: 1200px; height: 25px;
    background: var(--ink);
    display: flex; justify-content: center; align-items: center; gap: 25px;
    font-size: 11.5px;
  }
  .main-nav a { color: var(--white); text-decoration: none; }
  .main-nav a.is-current { color: var(--gold); }
  .content {
    position: absolute; top: 247px; left: 0;
    width: 1200px; height: 510px;
    background: var(--paper);
  }
  .about {
    position: absolute; top: 22px; left: 246px; width: 476px;
  }
  .about h1 {
    text-align: center; color: var(--gold);
    font-size: 22px; font-weight: 400; line-height: 30px;
    padding-left: 26px;
    margin-bottom: 17px;
  }
  .about p {
    font-size: 11.3px; line-height: 15px;
    text-align: justify; margin-bottom: 15px;
  }
  .portrait {
    position: absolute; top: 25px; left: 746px;
    width: 208px; height: 460px;
    background: linear-gradient(180deg, var(--photo-light) 0%, #d9cfc8 35%, var(--photo-dark) 55%, #3f5274 100%);
  }
  .site-footer {
    position: absolute; top: 757px; left: 0; width: 1200px; height: 243px;
    color: var(--white);
  }
  .footer-brand {
    position: absolute; top: 80px; left: 246px;
    color: var(--gold); font-size: 16px;
  }
  .footer-block { position: absolute; top: 26px; font-size: 8px; line-height: 10.7px; }
  .footer-block h2 {
    color: var(--gold); font-size: 10.5px; font-weight: 400;
    margin-bottom: 8px; letter-spacing: 0.2px;
  }
  .contact-block { left: 515px; }
  .hours-block { left: 803px; width: 151px; }
  .hours-row { display: flex; justify-content: space-between; }
</style>
</head>
<body>
  <header class="site-header">
    <div class="brand-name">Ben Otrelu</div>
  </header>

  <nav class="main-nav">
    <a href="#">Home</a>
    <a href="#" class="is-current">About Me</a>
    <a href="#">Testimonials</a>
    <a href="#">Patient Resources</a>
    <a href="#">Contact</a>
  </nav>

  <main class="content">
    <section class="about">
      <h1>About Me</h1>
      <p>BDS (Hons) MUDF RGS (Eng)</p>
      <p>I am a Taffside University graduate and registered with the Dental Practice Council (DPC no. 318572)</p>
      <p>I provide care for my patients at Pencoed Dental Surgery, a state of the art private practice in Pencoed Village, Cardiff. I have a particular interest in periodontal disease and in restoring missing teeth with dental implants.</p>
      <p>I work as a Clinical Research Fellow and a Clinical Lecturer at Avonmere Dental Hospital, University of Avonmere. My research interests include developing research methodologies, periodontal conditions, bone augmentation and peri-implant lesions, the scientific evaluation of oral health care products, toothwear, dentine hypersensitivity and tooth whitening. I currently partake in clinical research studies with publications in peer-reviewed journals. I am involved with undergraduate teaching &amp; training of Periodontology at the University of Avonmere and I also lecture in the national forum.</p>
      <p>I am an active member of the Albion Society of Periodontology and Global Circle for Implantology. I am also a Member of the United Dental Faculties of the Royal Guild of Surgeons (England) and the Welsh representative on the committee for the Fellowship of Dental Implantology.</p>
      <p>I enjoy working with my patients in order to meet their oral health requirements and I appreciate that one's experiences and circumstances are fundamental to understanding their dental needs. I, therefore, believe in a holistic and specific approach tailored to each patient, from the nervous individual to those looking to improve their smile.</p>
      <p>If you would like to find out more about how I could help you, please get in touch.</p>
    </section>
    <div class="portrait" role="img" aria-label="Portrait photograph of the dentist in blue scrubs, seated at a desk"></div>
  </main>

  <footer class="site-footer">
    <div class="footer-brand">Ben Otrelu</div>
    <div class="footer-block contact-block">
      <h2>GET IN TOUCH</h2>
      <div>Pencoed Dental Surgery</div>
      <div>41-43 Ffordd Glas</div>
      <div>Cardiff</div>
      <div>CF23 9QL</div>
      <div>&nbsp;</div>
      <div>029 2048 3170</div>
    </div>
    <div class="footer-block hours-block">
      <h2>PENCOED OPENING TIMES</h2>
      <div class="hours-row"><span>Monday</span><span>8.00am - 8.00pm</span></div>
      <div class="hours-row"><span>Tuesday</span><span>8.00am - 8.00pm</span></div>
      <div class="hours-row"><span>Wednesday</span><span>8.00am - 8.00pm</span></div>
      <div class="hours-row"><span>Thursday</span><span>8.00am - 8.00pm</span></div>
      <div class="hours-row"><span>Friday</span><span>8.00am - 5.30pm</span></div>
      <div class="hours-row"><span>Saturday</span><span>8.15am - 4.30pm</span></div>
    </div>
  </footer>
</body>
</html>
```